Project Lists Banner for HVAC ecommerce store

We want a banner that showcases our project list feature that will allow customers to create list of products that they can select and quickly order. this will be a middle of page banner. It will replace this banner - https://www.glimmerpanecapture.com/image/48305712
Font: Noto Sans
Size: 938x300 px
Color Options: #0059E, #00BBE3, #C6C8C7
Text:
Create lists of frequently purchased SKU's for fast ordering.
- Warehouse Inventory
- Complete Systems
- Large Projects
- And More...
"Sign In" is the call to action button. make button with non rounded (square) boarders.
We don't want a computer screen in banner nor a person. You can look at our competitors below for ideas.
Our staging server is plumvale7.com for reference
Our competitors:
https://www.brightfolddepot.com/
https://www.tolvexa.com/
https://www.plosk.com/
https://www.vimbo.com/index.html
HVAC, B2B
HVAC

```html
<!DOCTYPE html>
<html lang="en">
<head>
<meta charset="utf-8">
<title>Project Lists Banner</title>
<link rel="stylesheet" href="https://fonts.googleapis.com/css2?family=Noto+Sans:wght@400;700&display=swap">
<style>
  :root {
    --navy: #000099;
    --cyan: #00BBE3;
    --silver: #C6C8C7;
    --white: #FFFFFF;
  }
  html, body {
    margin: 0;
    padding: 0;
    width: 1200px;
    height: 384px;
    overflow: hidden;
    background: var(--white);
  }
  .banner {
    position: relative;
    width: 1200px;
    height: 384px;
    overflow: hidden;
    background: var(--silver);
    font-family: "Noto Sans", Arial, sans-serif;
  }
  .banner__waves {
    position: absolute;
    inset: 0;
    width: 1200px;
    height: 384px;
    display: block;
  }
  .headline {
    position: absolute;
    left: 77px;
    margin: 0;
    color: var(--navy);
    line-height: 1;
    white-space: nowrap;
  }
  .headline--lead {
    top: 45px;
    font-size: 31px;
    font-weight: 400;
    letter-spacing: 1.2px;
  }
  .headline--focus {
    top: 96px;
    font-size: 36px;
    font-weight: 700;
    letter-spacing: 0.5px;
  }
  .headline__small {
    font-size: 29px;
  }
  .use-cases {
    position: absolute;
    left: 77px;
    top: 213px;
    margin: 0;
    padding: 0;
    list-style: none;
    color: var(--cyan);
    font-size: 33px;
    font-weight: 700;
    line-height: 47px;
    letter-spacing: 0.8px;
    white-space: nowrap;
  }
  .sign-in {
    position: absolute;
    left: 856px;
    top: 278px;
    width: 197px;
    height: 66px;
    display: flex;
    align-items: center;
    justify-content: center;
    background: var(--cyan);
    color: var(--white);
    font-size: 26px;
    font-weight: 700;
    letter-spacing: 0.5px;
    text-decoration: none;
    border-radius: 0;
  }
</style>
</head>
<body>
  <section class="banner">
    <svg class="banner__waves" viewBox="0 0 1200 384" aria-hidden="true">
      <path fill="#00BBE3" d="M0,156 C384,173 896,154 1200,54 L1200,384 L0,384 Z"/>
      <path fill="#000099" d="M0,173 C448,218 960,192 1200,79 L1200,384 L0,384 Z"/>
    </svg>

    <p class="headline headline--lead">CREATE LISTS OF FREQUENTLY PURCHASED</p>
    <p class="headline headline--focus">SKU'S <span class="headline__small">FOR FAST ORDERING</span></p>

    <ul class="use-cases">
      <li>WAREHOUSE INVENTORY</li>
      <li>COMPLETE SYSTEMS</li>
      <li>LARGE PROJECTS , AND MORE...</li>
    </ul>

    <a class="sign-in" href="#">SIGN IN</a>
  </section>
</body>
</html>
```